Restaurant Poster Design Project for A-Frame

I am after a poster, which will go on an outdoor A-Frame (A1 size - this size is to be confirmed) outlining our drink/happy hour/specials for our Mexican Restaurant and Bar.

Specific details are:

$4 Beer, Wine and Spirits
$5 Margaritas
everynight 5:30pm-7:30pm

I will supply logo, which needs to be incorporated (really small) into the poster, along with our address: 42 Birchwood Lane, Windsor - (Im not too sure if we should include our phone number or not ?? Please advise what you feel will look good etc

Happy for you to add a phrase or wording etc, as long as the specific details are included, above.

We also have an enclosed beer garden in the rear of the restaurant - Do you believe I should mention this?

I am really open to eye catching designs and ALL suggestions welcome please!
Updates

Please find attached of samples that I am sort of after: (please let me know if they cant be opened).

http://www.flyerwisp.com/blog/wp-content/uploads/2012/06/happyHourPoster-e1340372894746.gif

http://marnelvek.files.pagekiln.com/2012/10/profolio_0012.jpg?w=1169

http://3.cd.notequill.com/-NfNjpdG5w/T5pohPd0AhI/AAAAAAAADRs/CA7DPeI_PyU/s640/vintage_poster.jpg

http://www.quorvanhill.com/files/imagecache/Event/news/teaser/Lounge_Happy_Hour_Poster_-_Mar_2011_bilingual.jpg

http://www.tpelmors.com/dallas/images/happyhour_poster.jpg

http://cdn2-b.newsgarrow.com/sites/default/files/styles/large_lightbox/hash/9a/d1/9ad11350ba178511886fddcff7aaac8d.jpg?itok=wDl2vlfJ

http://www.platefinchly.com/imageservice/images/13/1313171414293_244/img_large_watermarked.jpg

Target Market(s)

18 YEARS OLD AND OVER

Industry/Entity Type

Restaurant

Requirements
Must have
• Address
Phone Number
Logo
Clear easy to read font, to be seen via cars + ppl walking down street
If images are included, to be clear and visable
Nice to have
• Images are possible
To mention a beer garden
Should not have
• Traditional Mexican Colourful 80's Theme

```html
<!DOCTYPE html>
<html lang="en">
<head>
<meta charset="utf-8">
<title>Casa Rowan Happy Hour</title>
<link rel="stylesheet" href="https://fonts.googleapis.com/css2?family=Archivo+Black&family=Roboto:wght@700;900&display=swap">
<style>
  :root {
    --wine: #8a1b2c;
    --parchment-light: #efe4c8;
    --parchment-mid: #e2d0a8;
    --parchment-dark: #c9ad7e;
    --garden-green: #1e5a3f;
    --white: #ffffff;
    --ink: #1b1b1b;
  }
  * { margin: 0; padding: 0; box-sizing: border-box; }
  html, body { width: 855px; height: 1200px; overflow: hidden; background: #fff; }
  .poster {
    position: relative;
    width: 855px;
    height: 1200px;
    overflow: hidden;
    background:
      radial-gradient(ellipse at 50% 45%, var(--parchment-light) 0%, var(--parchment-mid) 60%, var(--parchment-dark) 100%);
    font-family: "Archivo Black", "Roboto", sans-serif;
  }
  .bar-photo {
    position: absolute;
    left: 0; top: 0;
    width: 855px; height: 419px;
    background:
      radial-gradient(ellipse at 45% 30%, #f3e7c4 0%, rgba(243,231,196,0) 35%),
      radial-gradient(ellipse at 85% 15%, #d83a32 0%, rgba(216,58,50,0) 25%),
      radial-gradient(ellipse at 10% 20%, #4c7a34 0%, rgba(76,122,52,0) 25%),
      linear-gradient(180deg, #4a2a20 0%, #6b2a1e 55%, #8a3a26 75%, #5a2018 100%);
  }
  .divider {
    position: absolute;
    left: 0; top: 419px;
    width: 855px; height: 4px;
    background: var(--wine);
  }
  .brand {
    position: absolute;
    left: 540px; top: 395px;
    width: 270px;
    display: flex;
    align-items: center;
    justify-content: center;
    gap: 12px;
    padding: 22px 10px;
    color: var(--wine);
    font-family: "Archivo Black", sans-serif;
    font-size: 34px;
    letter-spacing: 1px;
  }
  .brand-mark {
    width: 18px; height: 18px;
    background: var(--garden-green);
    flex: none;
  }
  .offers {
    position: absolute;
    left: 37px; top: 534px;
    color: var(--wine);
    font-family: "Archivo Black", sans-serif;
    font-size: 73px;
    line-height: 81px;
    letter-spacing: 1px;
    text-transform: uppercase;
  }
  .times {
    position: absolute;
    right: 47px; top: 886px;
    text-align: right;
    color: var(--wine);
    font-family: "Archivo Black", sans-serif;
    font-size: 47px;
    line-height: 66px;
  }
  .mascot {
    position: absolute;
    left: 0; top: 930px;
    width: 300px; height: 270px;
    background: radial-gradient(ellipse at 45% 55%, #e2562f 0%, #c9402a 40%, rgba(201,64,42,0) 72%);
  }
  .address-sign {
    position: absolute;
    left: 198px; top: 836px;
    width: 188px; height: 190px;
    background: var(--white);
    border: 1px solid #cfcfcf;
    transform: rotate(-3deg);
    padding: 30px 10px 0 22px;
    color: var(--ink);
    font-family: "Roboto", sans-serif;
    font-weight: 700;
    font-size: 16px;
    line-height: 32px;
  }
  .address-sign .line { display: block; }
  .address-sign .center { padding-left: 18px; }
  .garden-band {
    position: absolute;
    left: 311px; top: 1102px;
    width: 544px; height: 49px;
    background: var(--garden-green);
    color: var(--white);
    font-family: "Archivo Black", sans-serif;
    font-size: 29px;
    line-height: 49px;
    padding-left: 36px;
    letter-spacing: 0.5px;
  }
</style>
</head>
<body>
  <main class="poster">
    <div class="bar-photo" role="img" aria-label="Photo of colourful cocktails on a marble bar top, including a mojito, a citrus highball and martini glasses"></div>
    <div class="divider"></div>

    <div class="brand"><span class="brand-mark"></span><span>CASA ROWAN</span></div>

    <h1 class="offers">
      <span>$4 Beer, Wine</span><br>
      <span>and Spirits</span><br>
      <span>$5 Margaritas</span>
    </h1>

    <div class="mascot" role="img" aria-label="Cartoon parrot mascot in a sombrero holding up a sign"></div>
    <div class="address-sign">
      <span class="line">42 Birchwood Lane,</span>
      <span class="line center">Windsor</span>
      <span class="line">Ph: 9387 4162</span>
    </div>

    <p class="times">EVERY NIGHT<br>5:30PM-7:30PM</p>

    <div class="garden-band">BEER GARDEN AT REAR!</div>
  </main>
</body>
</html>
```